One Page Website for Personal Trainer in London

I have a logo and need a one page website designed around my branding. I am a freelance Personal Trainer based in London specialising in bodyweight training for men and women. I would like the site to be modern and clean but not overtly urban in design.
I need the following headings:
About Me
My Services
Events
Blog
I don't need them to be seperate pages but if they can link to further down the page that would be great.
Industry/Entity Type
Personal Trainer
Coding
Coded - Design and coding required
Number of Pages Required
1 page
Requirements
Must have
- I need the following headings:
- About Me
- My Services
- Events
- Blog
- mobile friendly formatting
- health and fitness related photography
- Colour scheme in keeping with my existing logo

```html
<!DOCTYPE html>
<html lang="en">
<head>
<meta charset="utf-8">
<title>Marlowe Kent — Personal Training</title>
<link href="https://fonts.googleapis.com/css2?family=Roboto:wght@400;500;700;900&display=swap" rel="stylesheet">
<style>
:root{
  --orange:#f7931e;
  --black:#0d0d0d;
  --dark:#1a1a1a;
  --footer:#161616;
  --light:#f2f2f2;
  --white:#ffffff;
  --text:#555555;
  --muted:#8a8a8a;
}
*{box-sizing:border-box;margin:0;padding:0}
html,body{width:1200px;height:3905px;overflow:hidden}
body{position:relative;font-family:'Roboto',Arial,sans-serif;color:var(--text);background:var(--white)}
section,header,footer{position:absolute;left:0;width:1200px;overflow:hidden}
.wrap{position:absolute;left:234px;width:732px}
h2{font-weight:700;text-transform:uppercase;letter-spacing:.5px}
p{font-size:11px;line-height:17px}
.btn{display:inline-block;font-size:9px;font-weight:700;text-transform:uppercase;letter-spacing:.6px;text-align:center;line-height:30px;height:32px}
.btn-outline{border:2px solid var(--white);color:var(--white)}
.btn-orange{background:var(--orange);color:var(--white)}
.btn-black{background:var(--black);color:var(--white)}

/* nav */
.site-nav{top:0;height:65px;background:rgba(0,0,0,.92);z-index:5}
.brand{position:absolute;left:234px;top:14px;display:flex;align-items:center;gap:8px}
.brand-mark{width:22px;height:22px;background:var(--orange)}
.brand-name{font-size:17px;font-weight:700;color:var(--white)}
.brand-sub{position:absolute;left:30px;top:25px;font-size:7px;letter-spacing:2px;color:var(--white);white-space:nowrap}
.menu{position:absolute;right:234px;top:26px;display:flex;gap:26px;list-style:none}
.menu li{font-size:9px;font-weight:700;color:var(--white);letter-spacing:.4px}
.menu li.active{color:var(--orange)}

/* hero */
.hero{top:0;height:612px}
.hero-photo{position:absolute;inset:0;background:linear-gradient(180deg,#4a4440 0%,#2d2a28 50%,#3b3633 100%)}
.hero-frame{position:absolute;left:513px;top:213px;width:170px;height:177px;border:6px solid var(--orange)}
.hero-title{position:absolute;top:262px;width:100%;text-align:center;color:var(--white);font-size:36px;font-weight:700;letter-spacing:1px}
.hero-sub{position:absolute;top:315px;width:100%;text-align:center;color:var(--white);font-size:19px;font-weight:700}
.hero-arrow{position:absolute;top:320px;width:30px;height:30px;border:1px solid rgba(255,255,255,.6);display:flex;align-items:center;justify-content:center}
.hero-arrow.left{left:31px}.hero-arrow.right{right:31px}
.hero-dots{position:absolute;top:568px;width:100%;text-align:center;color:var(--white);font-size:11px;font-weight:700;word-spacing:12px}

/* about */
.about{top:612px;height:372px;background:var(--orange)}
.about-photo{position:absolute;top:0;left:0;width:1200px;height:372px;background:linear-gradient(180deg,#5d87a6 0%,#7fa6c0 45%,#c9b49a 75%,#b69b7c 100%);clip-path:polygon(650px 0,1200px 0,1200px 372px,555px 372px)}
.about h2{position:absolute;left:234px;top:58px;color:var(--white);font-size:17px}
.about p{position:absolute;left:234px;width:300px;color:var(--white)}
.about .btn{position:absolute;left:234px;top:276px;width:120px}

/* features */
.features{top:984px;height:252px;background:var(--black)}
.feature{position:absolute;top:80px;width:170px;text-align:center}
.feature h3{margin-top:12px;font-size:9px;font-weight:700;color:var(--white);text-transform:uppercase}
.feature p{margin-top:6px;font-size:9px;line-height:13px;color:#b5b5b5}

/* services */
.services{top:1236px;height:373px;background:var(--orange)}
.services-photo{position:absolute;inset:0;background:linear-gradient(90deg,#2a2a2a 0%,#4b4b4b 45%,#6a6a6a 100%);clip-path:polygon(0 0,650px 0,547px 373px,0 373px)}
.services h2{position:absolute;left:672px;top:60px;color:var(--white);font-size:17px}
.svc-arrows{position:absolute;left:916px;top:60px;display:flex;gap:6px}
.svc-arrows span{width:20px;height:20px;border:1px solid rgba(255,255,255,.7)}
.svc{position:absolute;left:672px;width:300px}
.svc svg{position:absolute;left:0;top:0}
.svc h3{margin-left:42px;font-size:9px;font-weight:700;color:var(--white);text-transform:uppercase}
.svc p{margin-left:42px;margin-top:6px;font-size:9px;line-height:13px;color:var(--white)}

/* cards */
.listing{background:var(--light)}
.events{top:1609px;height:531px}
.blog{top:2650px;height:547px}
.listing h2{position:absolute;top:82px;width:100%;text-align:center;color:var(--black);font-size:18px}
.card{position:absolute;top:127px;width:232px}
.card-photo{position:relative;height:172px}
.date{position:absolute;right:0;top:0;width:36px;height:38px;background:var(--orange);color:var(--white);text-align:center;font-size:8px;font-weight:700;line-height:11px;padding-top:7px}
.date b{display:block;font-size:12px}
.card h3{margin-top:22px;font-size:9px;font-weight:700;color:var(--black);text-transform:uppercase}
.card p{margin-top:10px;font-size:9px;line-height:13px}
.read{margin-top:10px;font-size:8px;font-weight:700;color:var(--black);display:flex;align-items:center;gap:8px}
.listing .btn{position:absolute;left:539px;width:120px}

/* banner */
.banner{top:2140px;height:385px;background:var(--black)}
.banner-photo{position:absolute;inset:0;background:linear-gradient(90deg,#0f0f0f 0%,#1e1e1e 40%,#3a3a3a 70%,#2a2a2a 100%)}
.banner h2{position:absolute;left:234px;top:130px;width:600px;color:var(--white);font-size:24px;line-height:32px}
.banner p{position:absolute;left:234px;top:238px;width:400px;color:#d0d0d0;font-size:10px;line-height:15px}

/* cta */
.cta{top:2525px;height:125px;background:var(--orange)}
.cta h3{position:absolute;left:234px;top:43px;font-size:13px;font-weight:700;color:var(--white);text-transform:uppercase}
.cta p{position:absolute;left:234px;top:68px;font-size:9px;color:var(--white)}
.cta .btn{position:absolute;left:849px;top:46px;width:117px}

/* contact */
.contact{top:3197px;height:390px;background:var(--dark)}
.contact-photo{position:absolute;inset:0;background:linear-gradient(90deg,#2b2b2b 0%,#3c3c3c 55%,#262626 100%)}
.contact-panel{position:absolute;inset:0;background:var(--orange);clip-path:polygon(0 0,650px 0,534px 390px,0 390px)}
.contact h2{position:absolute;left:234px;top:64px;color:var(--white);font-size:16px}
.field{position:absolute;left:234px;width:294px;height:30px;border:1px solid rgba(255,255,255,.7);color:var(--white);font-size:9px;padding:9px 12px}
.contact .btn{position:absolute;left:234px;top:294px;width:118px}

/* footer */
.site-footer{top:3587px;height:318px;background:var(--footer)}
.fcol{position:absolute;top:58px;width:170px}
.fcol h4{font-size:9px;font-weight:700;color:var(--white);text-transform:uppercase;margin-bottom:16px}
.fcol p{font-size:8px;line-height:12px;color:var(--muted)}
.post{display:flex;gap:8px;margin-bottom:12px;align-items:flex-start}
.post i{display:block;width:26px;height:22px;background:#444;flex:none}
.post span{font-size:8px;line-height:11px;color:#bdbdbd}
.social{margin-top:14px;display:flex;gap:12px}
.social span{width:8px;height:8px;border-radius:50%;background:#bdbdbd}
.contact-line{display:flex;gap:10px;align-items:center;font-size:8px;color:#bdbdbd;margin-bottom:10px}
.copy{position:absolute;left:0;top:271px;width:100%;border-top:1px solid #2b2b2b;text-align:center;padding-top:16px;font-size:8px;color:var(--muted)}
</style>
</head>
<body>

<header class="site-nav">
  <div class="brand"><span class="brand-mark"></span><span class="brand-name">Marlowe Kent</span><span class="brand-sub">PERSONAL TRAINING</span></div>
  <ul class="menu">
    <li class="active">HOME</li><li>ABOUT ME</li><li>SERVICES</li><li>EVENTS</li><li>BLOG</li><li>CONTACT US</li>
  </ul>
</header>

<section class="hero">
  <div class="hero-photo" role="img" aria-label="Athlete in a push-up start position in a dim brick-walled gym"></div>
  <div class="hero-frame"></div>
  <h1 class="hero-title">FIGHT TILL THE END</h1>
  <div class="hero-sub">PAIN IS TEMPORARY, GLORY IS FOREVER!</div>
  <div class="hero-arrow left"><svg width="10" height="10" viewBox="0 0 10 10"><path d="M7 1 3 5l4 4" stroke="#fff" fill="none" stroke-width="1.4"/></svg></div>
  <div class="hero-arrow right"><svg width="10" height="10" viewBox="0 0 10 10"><path d="M3 1l4 4-4 4" stroke="#fff" fill="none" stroke-width="1.4"/></svg></div>
  <div class="hero-dots">01 02 03</div>
</section>

<section class="about" id="about">
  <div class="about-photo" role="img" aria-label="Trainer standing on a sunny beach by the sea"></div>
  <h2>About Me</h2>
  <p style="top:104px">Bodyweight coaching for men and women across London. I build strength, mobility and confidence with simple sessions you can repeat anywhere, no machines needed, just steady progress and honest support every week.</p>
  <p style="top:198px">Every plan starts with a chat about your goals, your routine and your history, then grows with you as you get fitter and stronger.</p>
  <span class="btn btn-outline">More About Me</span>
</section>

<section class="features">
  <div class="feature" style="left:234px">
    <svg width="26" height="26" viewBox="0 0 26 26" fill="none" stroke="#fff" stroke-width="1.6"><path d="M4 16v-3a9 9 0 0 1 18 0v3"/><rect x="3" y="15" width="5" height="7" rx="1"/><rect x="18" y="15" width="5" height="7" rx="1"/></svg>
    <h3>Free Consultation</h3><p>A relaxed first meeting to talk goals, history and the best way to start.</p>
  </div>
  <div class="feature" style="left:422px">
    <svg width="26" height="26" viewBox="0 0 26 26" fill="none" stroke="#fff" stroke-width="1.6"><path d="M13 2l3.3 7 7.5.8-5.6 5 1.6 7.4L13 18.4l-6.8 3.8 1.6-7.4-5.6-5 7.5-.8z"/></svg>
    <h3>Excellent Service</h3><p>Clear plans, quick replies and sessions that fit around your week.</p>
  </div>
  <div class="feature" style="left:609px">
    <svg width="26" height="26" viewBox="0 0 26 26" fill="none" stroke="#fff" stroke-width="1.6"><path d="M4 3h18l-7 10v7h-4v-7z"/><path d="M8 23h10"/></svg>
    <h3>Best Trainers</h3><p>Qualified coaching focused on safe form and steady lasting gains.</p>
  </div>
  <div class="feature" style="left:797px">
    <svg width="26" height="26" viewBox="0 0 26 26" fill="none" stroke="#fff" stroke-width="1.6"><path d="M8 12h-4v11h4zM8 12l4-8c2 0 3 1 3 3l-1 4h7c1.5 0 2.5 1.3 2 2.6l-2.5 7.5c-.4 1.1-1.3 1.9-2.5 1.9H8"/></svg>
    <h3>Work Programs</h3><p>Structured bodyweight programs you can follow at home or outdoors.</p>
  </div>
</section>

<section class="services" id="services">
  <div class="services-photo" role="img" aria-label="Man curling a dumbbell in front of a weight rack"></div>
  <h2>Services</h2>
  <div class="svc-arrows"><span></span><span></span></div>
  <div class="svc" style="top:112px">
    <svg width="28" height="18" viewBox="0 0 28 18" fill="none" stroke="#fff" stroke-width="1.6"><path d="M2 6v6M6 3v12M22 3v12M26 6v6M6 9h16"/></svg>
    <h3>Personal Training</h3><p>One to one sessions built around your body, your goals and your schedule.</p>
  </div>
  <div class="svc" style="top:196px">
    <svg width="26" height="22" viewBox="0 0 26 22" fill="none" stroke="#fff" stroke-width="1.6"><circle cx="9" cy="7" r="4"/><circle cx="19" cy="8" r="3"/><path d="M2 20c0-4 3-6 7-6s7 2 7 6M16 14c4 0 8 1 8 5"/></svg>
    <h3>Group Programs</h3><p>Small outdoor groups with a friendly pace and plenty of coaching.</p>
  </div>
  <div class="svc" style="top:284px">
    <svg width="22" height="22" viewBox="0 0 22 22" fill="none" stroke="#fff" stroke-width="1.6"><circle cx="11" cy="12" r="8"/><path d="M11 12V7M9 2h4"/></svg>
    <h3>Fitness Testing</h3><p>Simple checks to track strength, mobility and endurance over time.</p>
  </div>
</section>

<section class="listing events" id="events">
  <h2>Upcoming Events</h2>
  <div class="card" style="left:234px">
    <div class="card-photo" role="img" aria-label="Athlete stretching in a gym" style="background:linear-gradient(135deg,#4a4a4a,#8a8a8a)"><div class="date">JUN<b>05</b></div></div>
    <h3>Summer Team Games 2017</h3><p>A morning of relays and partner drills in the park, open to every level of fitness.</p>
    <div class="read">READ MORE <svg width="12" height="6" viewBox="0 0 12 6"><path d="M0 3h11M8 0l3 3-3 3" stroke="#000" fill="none"/></svg></div>
  </div>
  <div class="card" style="left:484px">
    <div class="card-photo" role="img" aria-label="Woman training on a gym bench" style="background:linear-gradient(135deg,#3a3a3a,#9a6060)"><div class="date">JUN<b>11</b></div></div>
    <h3>Absolute Summer Activities</h3><p>Outdoor circuits, core work and a cool down by the river on long summer evenings.</p>
    <div class="read">READ MORE <svg width="12" height="6" viewBox="0 0 12 6"><path d="M0 3h11M8 0l3 3-3 3" stroke="#000" fill="none"/></svg></div>
  </div>
  <div class="card" style="left:734px">
    <div class="card-photo" role="img" aria-label="Woman resting after a gym session" style="background:linear-gradient(135deg,#6a6a6a,#c9c0b5)"><div class="date">JUN<b>15</b></div></div>
    <h3>Special Training From Marlowe</h3><p>A focused workshop on push-up, squat and plank technique with personal feedback.</p>
    <div class="read">READ MORE <svg width="12" height="6" viewBox="0 0 12 6"><path d="M0 3h11M8 0l3 3-3 3" stroke="#000" fill="none"/></svg></div>
  </div>
  <span class="btn btn-orange" style="top:437px">All Events</span>
</section>

<section class="banner">
  <div class="banner-photo" role="img" aria-label="Woman training on a rowing machine in a dark gym"></div>
  <h2>Nam elit arcu, malesuada id ornare nec, pellentesque ut augue.</h2>
  <p>Strength is built one session at a time. Show up, move well and rest well, and the results will follow. Train with purpose, keep it simple and enjoy getting stronger every single week.</p>
</section>

<section class="cta">
  <h3>Got a question? We would be happy to help!</h3>
  <p>Send a short message and I will get back to you within one day.</p>
  <span class="btn btn-outline">Contact Us</span>
</section>

<section class="listing blog" id="blog">
  <h2>Latest Blog</h2>
  <div class="card" style="left:234px">
    <div class="card-photo" role="img" aria-label="Man lifting a barbell" style="background:linear-gradient(135deg,#3a3a3a,#8a7a6a)"><div class="date">JUN<b>05</b></div></div>
    <h3>Easily Increase Your Muscle Mass in 10 Steps</h3><p>Ten simple habits that help you build muscle with bodyweight work and good recovery.</p>
    <div class="read">READ MORE <svg width="12" height="6" viewBox="0 0 12 6"><path d="M0 3h11M8 0l3 3-3 3" stroke="#000" fill="none"/></svg></div>
  </div>
  <div class="card" style="left:484px">
    <div class="card-photo" role="img" aria-label="Woman lifting weights in a gym" style="background:linear-gradient(135deg,#5a5a5a,#b0a8a0)"><div class="date">JUN<b>11</b></div></div>
    <h3>10 Ways to Lose Stubborn Belly Fat</h3><p>Practical tips on movement, sleep and food to shift the last few pounds for good.</p>
    <div class="read">READ MORE <svg width="12" height="6" viewBox="0 0 12 6"><path d="M0 3h11M8 0l3 3-3 3" stroke="#000" fill="none"/></svg></div>
  </div>
  <div class="card" style="left:734px">
    <div class="card-photo" role="img" aria-label="Two people doing floor exercises" style="background:linear-gradient(135deg,#4a4a4a,#9a9090)"><div class="date">JUN<b>15</b></div></div>
    <h3>Finding Highly Qualified Personal Trainers</h3><p>What to ask before you book, and how to spot a coach who suits your goals.</p>
    <div class="read">READ MORE <svg width="12" height="6" viewBox="0 0 12 6"><path d="M0 3h11M8 0l3 3-3 3" stroke="#000" fill="none"/></svg></div>
  </div>
  <span class="btn btn-orange" style="top:449px">View All</span>
</section>

<section class="contact" id="contact">
  <div class="contact-photo" role="img" aria-label="Woman doing a kettlebell exercise in a gym"></div>
  <div class="contact-panel"></div>
  <h2>Get In Touch</h2>
  <div class="field" style="top:117px">Your Name</div>
  <div class="field" style="top:169px">Your Email</div>
  <div class="field" style="top:221px;height:52px">Message</div>
  <span class="btn btn-black">Send Message</span>
</section>

<footer class="site-footer">
  <div class="fcol" style="left:234px">
    <h4>About Me</h4>
    <p>London based personal trainer focused on bodyweight strength for men and women. Friendly, flexible coaching for every level.</p>
    <div class="social"><span></span><span></span><span></span><span></span></div>
  </div>
  <div class="fcol" style="left:422px">
    <h4>Recent Posts</h4>
    <div class="post"><i></i><span>Easily Increase Your Muscle Mass in 10 Steps</span></div>
    <div class="post"><i></i><span>10 Ways to Lose Stubborn Belly Fat</span></div>
    <div class="post"><i></i><span>Finding Highly Qualified Personal Trainers</span></div>
  </div>
  <div class="fcol" style="left:609px">
    <h4>Upcoming Events</h4>
    <div class="post"><i></i><span>Summer Team Games 2017</span></div>
    <div class="post"><i></i><span>Absolute summer activities</span></div>
    <div class="post"><i></i><span>Special training for Marlowe</span></div>
  </div>
  <div class="fcol" style="left:797px">
    <h4>Contact Us</h4>
    <div class="contact-line"><svg width="9" height="9" viewBox="0 0 10 10"><path d="M2 1l2 2-1 1.5c.7 1.3 1.4 2 2.5 2.5L7 6l2 2-1.5 1.5C4 9 1 6 .5 2.5z" fill="#bdbdbd"/></svg>(0) 20 0000 1234</div>
    <div class="contact-line"><svg width="9" height="9" viewBox="0 0 10 10"><path d="M2 1l2 2-1 1.5c.7 1.3 1.4 2 2.5 2.5L7 6l2 2-1.5 1.5C4 9 1 6 .5 2.5z" fill="#bdbdbd"/></svg>(0) 20 0000 5678</div>
    <div class="contact-line"><svg width="9" height="9" viewBox="0 0 10 10"><rect x=".5" y="2" width="9" height="6" fill="none" stroke="#bdbdbd"/><path d="M.5 2 5 5.5 9.5 2" fill="none" stroke="#bdbdbd"/></svg>hello@marlowekent.fit</div>
    <div class="contact-line"><svg width="9" height="9" viewBox="0 0 10 10"><path d="M5 9.5S1.5 6 1.5 4a3.5 3.5 0 0 1 7 0c0 2-3.5 5.5-3.5 5.5z" fill="#bdbdbd"/></svg>12 Park Lane, London</div>
  </div>
  <div class="copy">© 2017 All Rights Reserved</div>
</footer>

</body>
</html>
```